Chestnut Farm Logo and Business Card

We need a new logo design and new business cards for a recently purchased mature Chestnut Farm in the south west of Western Australia, the farm is called Willowmere Glen, We will be adding value to the chestnuts by creating a range of chestnut products based on the fact that chestnuts are a healthy, gluten free product that is suited to the vegetarian market as well as the health food market. We will be selling the products through farmers markets, restaurants, health food stores and online. The final design should communicate a healthy modern down to earth image.
Updates

Sorry, I should have given the details for the business cards.

Address is 
Willowmere Glen
PO Box 417 
Karrowin, Westvale Shire, 6318

Email is 
willowmere.glen@fernpost.com

Website is
www.glenhollowfoods.com

Phone number is 
(08) 9412 7730

Many thanks

We would like to see the logo separate to the business card as well if possible please?

Industry/Entity Type

Farm

Logo Text

Willowmere Glen

```html
<!DOCTYPE html>
<html lang="en">
<head>
<meta charset="utf-8">
<title>Willowmere Glen – Business Cards</title>
<link rel="stylesheet" href="https://fonts.googleapis.com/css2?family=Bitter:wght@300;400&display=swap">
<style>
  :root {
    --farm-green: #35512a;
    --chestnut: #4a1418;
    --card-white: #ffffff;
    --card-edge: #1e1e1e;
    --page: #ffffff;
  }
  * { box-sizing: border-box; margin: 0; padding: 0; }
  html, body { width: 1200px; height: 1000px; overflow: hidden; background: var(--page); }
  body { position: relative; font-family: "Bitter", Georgia, serif; font-weight: 300; color: var(--chestnut); }

  .card {
    position: absolute;
    left: 296px;
    width: 579px;
    height: 325px;
    background: var(--card-white);
    border: 1px solid var(--card-edge);
  }
  .card--front { top: 130px; }
  .card--back { top: 521px; }

  .side-band {
    position: absolute;
    left: 0; top: 0; bottom: 0;
    width: 47px;
    background: var(--farm-green);
  }
  .band-icon {
    position: absolute;
    left: 11px;
    width: 24px;
    height: 24px;
    fill: none;
    stroke: #fff;
  }
  .band-icon--solid { fill: #fff; stroke: none; }

  .text { position: absolute; white-space: nowrap; line-height: 1; }

  .brand {
    position: absolute;
    display: flex;
    align-items: center;
    gap: 10px;
  }
  .brand-dot { border-radius: 50%; background: var(--farm-green); flex: none; }
  .brand-name { font-weight: 400; color: var(--chestnut); white-space: nowrap; line-height: 1; }

  .card--front .brand { right: 33px; top: 32px; }
  .card--front .brand-dot { width: 28px; height: 28px; }
  .card--front .brand-name { font-size: 26px; }

  .card--back .brand { left: 126px; top: 130px; }
  .card--back .brand-dot { width: 42px; height: 42px; }
  .card--back .brand-name { font-size: 38px; }

  .person-name { left: 0; width: 585px; text-align: center; top: 132px; font-size: 24px; font-weight: 400; }
  .person-role { left: 0; width: 578px; text-align: center; top: 160px; font-size: 16px; }

  .contact { font-size: 15px; left: 63px; }
  .contact--email { font-size: 14px; }
  .address { position: absolute; font-style: normal; font-size: 15px; line-height: 19px; left: 295px; top: 250px; white-space: nowrap; }
  .address--small { font-size: 12px; line-height: 15px; left: 351px; top: 23px; }

  .web-icon { position: absolute; width: 24px; height: 24px; fill: none; stroke: var(--chestnut); }
</style>
</head>
<body>

<section class="card card--front" aria-label="Business card front">
  <div class="side-band">
    <svg class="band-icon band-icon--solid" style="top:217px" viewBox="0 0 24 24" aria-hidden="true"><path d="M6.6 2.5c.6-.4 1.4-.3 1.8.3l2.2 3.3c.4.6.3 1.4-.3 1.8L8.9 8.8c.9 2.6 3.6 5.5 6.3 6.6l1-1.4c.4-.6 1.2-.8 1.8-.4l3.4 2.1c.6.4.8 1.2.4 1.8l-1.3 2c-.7 1.1-2 1.6-3.3 1.2C10.8 19 5 13.2 3.3 6.9 3 5.6 3.5 4.3 4.6 3.7z"/></svg>
    <svg class="band-icon" style="top:249px" viewBox="0 0 24 24" aria-hidden="true"><rect x="1" y="5" width="22" height="14" fill="#fff"/><path d="M1.5 5.5 12 13l10.5-7.5" stroke="var(--farm-green)" stroke-width="1.4"/></svg>
    <svg class="band-icon" style="top:281px" viewBox="0 0 24 24" stroke-width="1.4" aria-hidden="true"><circle cx="12" cy="12" r="10.5"/><ellipse cx="12" cy="12" rx="4.5" ry="10.5"/><path d="M1.5 12h21M12 1.5v21M3.5 6.5h17M3.5 17.5h17"/></svg>
  </div>

  <div class="brand">
    <span class="brand-dot"></span>
    <span class="brand-name">Willowmere Glen</span>
  </div>

  <p class="text person-name">Rowan Ellery</p>
  <p class="text person-role">Owner</p>

  <p class="text contact" style="top:220px">(08) 9412 7730</p>
  <p class="text contact contact--email" style="top:253px">willowmere.glen@fernpost.com</p>
  <p class="text contact" style="top:286px">www.glenhollowfoods.com</p>

  <address class="address">Willowmere Glen<br>PO Box 417<br>Karrowin, Westvale Shire, 6318</address>
</section>

<section class="card card--back" aria-label="Business card back">
  <div class="side-band">
    <svg class="band-icon band-icon--solid" style="top:241px" viewBox="0 0 24 24" aria-hidden="true"><path d="M6.6 2.5c.6-.4 1.4-.3 1.8.3l2.2 3.3c.4.6.3 1.4-.3 1.8L8.9 8.8c.9 2.6 3.6 5.5 6.3 6.6l1-1.4c.4-.6 1.2-.8 1.8-.4l3.4 2.1c.6.4.8 1.2.4 1.8l-1.3 2c-.7 1.1-2 1.6-3.3 1.2C10.8 19 5 13.2 3.3 6.9 3 5.6 3.5 4.3 4.6 3.7z"/></svg>
    <svg class="band-icon" style="top:273px" viewBox="0 0 24 24" aria-hidden="true"><rect x="1" y="5" width="22" height="14" fill="#fff"/><path d="M1.5 5.5 12 13l10.5-7.5" stroke="var(--farm-green)" stroke-width="1.4"/></svg>
  </div>

  <address class="address address--small">Willowmere Glen<br>PO Box 417<br>Karrowin, Westvale Shire, 6318</address>

  <div class="brand">
    <span class="brand-dot"></span>
    <span class="brand-name">Willowmere Glen</span>
  </div>

  <p class="text contact" style="top:244px">(08) 9412 7730</p>
  <p class="text contact contact--email" style="top:277px">willowmere.glen@fernpost.com</p>

  <svg class="web-icon" style="left:342px;top:271px" viewBox="0 0 24 24" stroke-width="1.4" aria-hidden="true"><circle cx="12" cy="12" r="10.5"/><ellipse cx="12" cy="12" rx="4.5" ry="10.5"/><path d="M1.5 12h21M12 1.5v21M3.5 6.5h17M3.5 17.5h17"/></svg>
  <p class="text contact" style="left:372px;top:276px">www.glenhollowfoods.com</p>
</section>

</body>
</html>
```